Coolant Fluid for Radiator BRISK VANE®

Its my first time working with Pixelharbor, and I want to see how it goes:)

We are needing a New exotic label design for our Brisk Vane ® Coolant Fluid for Radiators. Label if possible should be in

Spanish, but its ok if it is in English as we can edit the text later. This label should really stand out!

Front side of label:
Brand Name is BRISK VANE®

It's a Red Type Radiator Fluid/ Liquid. ( This Should Stand out)

It's also Triple action as it works as a Coolant,Anti Rust and Corrosion Inhibitor. It also Protects Aluminuim (Motor Block)

Its Special Red type and chemical composition help mantain the temperature at an optimum level thus preventing Overheating.

Bottle Capacity is 1 liter (Should be on front Label Bottom Right Side)

Back Side of Label:

Properties:
**Emphasizing that the product's Special Red type and chemical composition help mantain the temperature at an optimum

level thus preventing Overheating.
**Emphasize Triple Action (Mentioned above....)
**Will protect Plastic parts, and Connections.
**Mantain Low temperature.
**Prevent and Eliminate Build up of Calcium.

Instruction to use:
1. fill Radiator with BRISK VANE®
2. fill and Mix with Destilled water.

Dosing:
Small Cars 1Liter
Medium Cars 1Liter
Heavy Cars+Heavy Machinery 3Liter

As with almost all fluids for vehicles etc..Label should include safety Hazards.
Such as GHRB label (Please google it) ( Red Blue yellow and White ) Blue box should have a 1 and the others a Zero.

Health and Safety Hazards:
*If swallowed do not Induce vomiting
*seek for medical attention
*Poisonous if consumed
*Keep out of reach of children
(We will add some other things, that we are required to add)
Hazard Symbol Emphazising to read the manufacturer Instructions..

And a Small place where we can place a Barcode/ Recycable Symbol and Dispose of..
Product Registry Code, and Produced and Distributed by Lorem Ipsum etc..

I have attached some Bottle Designs,but dont Restrict yourself on these Bottles, Please keep in mind that the Bottle neck will be placed in the middle of the bottle and not to the sides as with most standard Oil Bottles.
If you have a better Idea/Outline of another bottle dont Hesitate to make a suggestion!

Thanks!
And Sorry my English is not the best :)
hope you have fun Designing this new Label!

Designs should be a little more something like these.. Please check the gallery, I uploaded some samples.. http://snapvault.example/album/zq81rt4k/ These are just for reference.. Regards,

Hi, Please Don't limit yourself to to the shape of the label. If you Think another shape would be better, please do. I will create a special bottle for your label. Thanks!

```html
<!DOCTYPE html>
<html lang="en">
<head>
<meta charset="utf-8">
<title>Brisk Vane Coolant Fluid – Front Label</title>
<link rel="stylesheet" href="https://fonts.googleapis.com/css2?family=Anton&family=Oswald:wght@500;700&display=swap">
<style>
  :root {
    --page: #ffffff;
    --label-deep: #2a0608;
    --label-mid: #5e0f14;
    --accent-red: #d8141e;
    --accent-light: #ff4a4f;
    --text-white: #ffffff;
    --check-grey: #bdbdbd;
    --sky-top: #3d7bb8;
    --sky-low: #b9d3ea;
    --truck-red: #c4221f;
    --car-dark: #1b1b1d;
    --car-grey: #8a8c90;
  }
  html, body {
    margin: 0;
    padding: 0;
    width: 778px;
    height: 1200px;
    overflow: hidden;
    background: var(--page);
  }
  .canvas {
    position: relative;
    width: 778px;
    height: 1200px;
  }
  .front-label {
    position: absolute;
    left: 190px;
    top: 340px;
    width: 420px;
    height: 750px;
    border-radius: 6px;
    overflow: hidden;
  }
  .label-art {
    position: absolute;
    inset: 0;
    width: 420px;
    height: 750px;
  }
  .brand-name {
    position: absolute;
    left: 0;
    top: 70px;
    width: 420px;
    margin: 0;
    font-family: "Anton", sans-serif;
    font-weight: 400;
    font-size: 142px;
    line-height: 146px;
    color: var(--text-white);
    text-align: center;
    letter-spacing: 1px;
  }
  .brand-name .word { display: block; }
  .brand-name .reg {
    font-size: 30px;
    vertical-align: top;
    line-height: 60px;
    margin-left: 2px;
  }
  .product-title {
    position: absolute;
    right: 8px;
    top: 388px;
    margin: 0;
    font-family: "Oswald", sans-serif;
    font-weight: 700;
    font-size: 42px;
    line-height: 44px;
    color: var(--text-white);
    text-align: right;
    text-transform: uppercase;
  }
  .benefits {
    position: absolute;
    right: 50px;
    top: 495px;
    margin: 0;
    padding: 0;
    list-style: none;
    font-family: "Oswald", sans-serif;
    font-weight: 500;
    font-size: 22px;
    line-height: 24px;
    color: var(--text-white);
    text-align: right;
  }
  .benefits li {
    position: relative;
    padding-right: 24px;
  }
  .benefits .tick {
    position: absolute;
    right: 0;
    top: 5px;
    width: 15px;
    height: 15px;
  }
  .capacity {
    position: absolute;
    right: 50px;
    top: 640px;
    font-family: "Oswald", sans-serif;
    font-weight: 700;
    color: var(--text-white);
    text-align: center;
  }
  .capacity .amount {
    display: block;
    font-size: 96px;
    line-height: 86px;
  }
  .capacity .unit {
    display: block;
    font-size: 20px;
    line-height: 22px;
  }
</style>
</head>
<body>
<main class="canvas">
  <section class="front-label">
    <svg class="label-art" viewBox="0 0 420 750" xmlns="http://www.w3.org/2000/svg">
      <defs>
        <radialGradient id="panelGlow" cx="0.6" cy="0.45" r="0.75">
          <stop offset="0" stop-color="var(--label-mid)"/>
          <stop offset="1" stop-color="var(--label-deep)"/>
        </radialGradient>
        <linearGradient id="truckScene" x1="0" y1="0" x2="0" y2="1">
          <stop offset="0" stop-color="var(--sky-top)"/>
          <stop offset="0.35" stop-color="var(--sky-low)"/>
          <stop offset="0.6" stop-color="var(--truck-red)"/>
          <stop offset="1" stop-color="#3c4a5a"/>
        </linearGradient>
        <linearGradient id="carScene" x1="0" y1="0" x2="1" y2="1">
          <stop offset="0" stop-color="var(--car-grey)"/>
          <stop offset="1" stop-color="var(--car-dark)"/>
        </linearGradient>
      </defs>

      <rect class="hex-panel" width="420" height="750" fill="url(#panelGlow)" role="img" aria-label="Dark red honeycomb texture background"/>

      <path class="truck-photo" d="M0 0 H390 L35 355 Q20 370 20 390 V655 L0 655 Z" fill="url(#truckScene)" role="img" aria-label="Photo of a red truck driving under a cloudy blue sky"/>

      <path class="car-photo" d="M0 655 L20 655 Q25 668 45 672 L420 745 V750 H0 Z" fill="url(#carScene)" role="img" aria-label="Photo of a dark car headlight"/>

      <path class="accent-curve" d="M390 0 L35 355 Q20 370 20 390 V640 Q20 668 48 673 L420 745" fill="none" stroke="var(--accent-red)" stroke-width="12"/>
      <path class="accent-highlight" d="M400 0 L44 357 Q31 372 31 392 V636 Q31 658 52 662 L420 734" fill="none" stroke="var(--accent-light)" stroke-width="2" opacity="0.7"/>
      <path class="corner-band" d="M372 0 H420 V44 Z" fill="var(--accent-red)"/>
    </svg>

    <h1 class="brand-name">
      <span class="word">BRISK<span class="reg">®</span></span>
      <span class="word">VANE</span>
    </h1>

    <h2 class="product-title">Coolant Fluid<br>for Radiators</h2>

    <ul class="benefits">
      <li>COOLANT<svg class="tick" viewBox="0 0 15 15"><rect x="1" y="1" width="13" height="13" fill="none" stroke="var(--check-grey)" stroke-width="1.5"/><path d="M3.5 7.5 L6.5 10.5 L12 3.5" fill="none" stroke="var(--check-grey)" stroke-width="2"/></svg></li>
      <li>ANTI RUST<svg class="tick" viewBox="0 0 15 15"><rect x="1" y="1" width="13" height="13" fill="none" stroke="var(--check-grey)" stroke-width="1.5"/><path d="M3.5 7.5 L6.5 10.5 L12 3.5" fill="none" stroke="var(--check-grey)" stroke-width="2"/></svg></li>
      <li>CORROSION INHIBITOR<svg class="tick" viewBox="0 0 15 15"><rect x="1" y="1" width="13" height="13" fill="none" stroke="var(--check-grey)" stroke-width="1.5"/><path d="M3.5 7.5 L6.5 10.5 L12 3.5" fill="none" stroke="var(--check-grey)" stroke-width="2"/></svg></li>
      <li>PROTECTS ALUMINUIM<svg class="tick" viewBox="0 0 15 15"><rect x="1" y="1" width="13" height="13" fill="none" stroke="var(--check-grey)" stroke-width="1.5"/><path d="M3.5 7.5 L6.5 10.5 L12 3.5" fill="none" stroke="var(--check-grey)" stroke-width="2"/></svg></li>
    </ul>

    <div class="capacity">
      <span class="amount">1</span>
      <span class="unit">LITER</span>
    </div>
  </section>
</main>
</body>
</html>
```